Natural Light/Organic/Documentary Photography Business

I like a simple, approachable, feminine, earthy/organic feel. Earth/neutral tones, nothing too loud or obnoxious. I like the watercolor look. I don't want anything too trendy or something I'll get tired of after a couple months. As far as colors, I am much more a fan of cream/taupe/blue/green...not a fan of pink or purple at all.

Target Market(s)

Weddings & Families

Industry/Entity Type

Wedding Photography

Contact Information for Business Card

website, email, phone number

Font styles to use
Other font styles liked:
• Horizontes, Gotham

Colors

Designer to choose colors to be used in the design.

Requirements
Must have
• Website: www.meliskaverholt.com
• Phone: 482.319.6047
• Email: tessa@meliskaverholt.com
Nice to have
• I like the watercolor look but its not necessary. I like simple/earthy tones. Nothing too loud or distracting. Simple & feminine without being too girly. I like an approachable/soft feel.
• Instagram: www.instagram.com/meliskaverholtphotography/
Should not have
• NO loud colors or design or pattern. I do not want a photo of a camera or lens or anything cheesy like that.

```html
<!DOCTYPE html>
<html lang="en">
<head>
<meta charset="utf-8">
<title>Meliska Verholt Photography – Business Card</title>
<link href="https://fonts.googleapis.com/css2?family=Cutive&display=swap" rel="stylesheet">
<style>
  :root {
    --backdrop: #efefef;
    --mint: #b6d3b9;
    --wash-light: #d2d2d2;
    --wash-mid: #b8b8b8;
    --wash-dark: #a4a4a4;
    --ink: #5f6a61;
    --accent: #6e786f;
  }
  * { margin: 0; padding: 0; box-sizing: border-box; }
  html, body {
    width: 1200px;
    height: 900px;
    overflow: hidden;
    background: var(--backdrop);
  }
  .canvas {
    position: relative;
    width: 1200px;
    height: 900px;
  }
  .card {
    position: absolute;
    left: 370px;
    top: 130px;
    width: 460px;
    height: 640px;
    background: var(--mint);
    overflow: hidden;
    font-family: "Cutive", Georgia, serif;
    color: var(--ink);
  }
  .card__wash {
    position: absolute;
    left: 0;
    top: 0;
    width: 100%;
    height: 215px;
    background:
      radial-gradient(ellipse at 25% 40%, var(--wash-dark) 0%, transparent 55%),
      radial-gradient(ellipse at 70% 70%, var(--wash-dark) 0%, transparent 50%),
      linear-gradient(160deg, var(--wash-light) 0%, var(--wash-mid) 60%, var(--wash-light) 100%);
  }
  .card__rule {
    position: absolute;
    right: 44px;
    top: 60px;
    width: 3px;
    height: 120px;
    background: var(--accent);
  }
  .brand {
    position: absolute;
    right: 30px;
    top: 196px;
    height: 250px;
    display: flex;
    flex-direction: row;
    align-items: flex-end;
    gap: 4px;
    writing-mode: vertical-rl;
    transform: rotate(180deg);
    white-space: nowrap;
  }
  .brand__name {
    font-size: 22px;
    letter-spacing: 0.5px;
    line-height: 24px;
  }
  .brand__tag {
    font-size: 9px;
    letter-spacing: 3px;
    line-height: 12px;
  }
  .card__marker {
    position: absolute;
    left: 22px;
    top: 440px;
    width: 18px;
    height: 62px;
    background: var(--accent);
  }
  .contact {
    position: absolute;
    left: 62px;
    top: 444px;
    list-style: none;
    font-size: 14px;
    letter-spacing: 0.8px;
    line-height: 24px;
    white-space: nowrap;
  }
  .contact__label {
    display: inline-block;
    width: 28px;
  }
</style>
</head>
<body>
<main class="canvas">
  <article class="card">
    <div class="card__wash" role="img" aria-label="Soft grey watercolor wash texture"></div>
    <span class="card__rule"></span>
    <div class="brand">
      <p class="brand__name">Meliska Verholt</p>
      <p class="brand__tag">PHOTOGRAPHY</p>
    </div>
    <span class="card__marker"></span>
    <ul class="contact">
      <li><span class="contact__label">W :</span>www.meliskaverholt.com</li>
      <li><span class="contact__label">P :</span>482.319.6047</li>
      <li><span class="contact__label">E :</span>tessa@meliskaverholt.com</li>
      <li><span class="contact__label">I :</span>@meliskaverholtphotography</li>
    </ul>
  </article>
</main>
</body>
</html>
```